Catering company looking to promote business

We need a flyer design for our company named "Berry Good Bites." We cater/deliver açaí bowls and smoothies.

The objective of this flyer is to let companies know that we are taking açaí bowls and smoothie orders and they can be delivered to them.

Some key points we would like on the flyer:
- Photo of açaí bowl and smoothie
- Menu w/ pricing
- "No hidden delivery fees"
- 5 bowl or smoothie minimum
- Online ordering through website:
https://shopkiosk.example/store/berrygoodbites
- For the month of February --> Get one free topping and drizzle!
- FRIDAY DELIVERIES ONLY
- Questions? Call (555) 417-9832
- social media chatterbook & snapgram @bgbites
- website www.berrygoodbites.example

font - hello beautiful

Target Market(s)

Juice, smoothies, açaí bowls

Industry/Entity Type

Business

Font styles to use
Other font styles liked:
• Hello Beautiful

Colors
a64599
b768aa
d3a5cc
eedced
f7f1f7
9bcb3c

Requirements
Must have
• Please match logo, fonts, color schemes, etc.

```html
<!DOCTYPE html>
<html lang="en">
<head>
<meta charset="utf-8">
<title>Berry Good Bites – Açaí Bowl Delivery Flyer</title>
<link rel="stylesheet" href="https://fonts.googleapis.com/css2?family=Amatic+SC:wght@700&family=Montserrat:wght@500;600;700&display=swap">
<style>
  :root {
    --plum: #5e3c93;
    --plum-deep: #6a4a9f;
    --orchid: #a64599;
    --mauve: #b768aa;
    --lilac: #d3a5cc;
    --blush: #e6c5df;
    --lavender: #c7b6da;
    --mist: #f7f1f7;
    --leaf: #9bcb3c;
    --leaf-deep: #5aa33a;
    --white: #ffffff;
    --hand: "Amatic SC", cursive;
    --body: "Montserrat", sans-serif;
  }
  * { margin: 0; padding: 0; box-sizing: border-box; }
  html, body { width: 960px; height: 1200px; overflow: hidden; background: var(--white); }
  .flyer {
    position: relative; width: 960px; height: 1200px; overflow: hidden;
    background: linear-gradient(180deg, #f1e3f0 0%, var(--white) 260px);
    font-family: var(--body);
  }
  .decor { position: absolute; inset: 0; }
  .brand {
    position: absolute; left: 58px; top: 114px; width: 290px; height: 290px;
    display: flex; align-items: center; justify-content: center; text-align: center;
    color: var(--plum); font-family: var(--body); font-weight: 700; font-size: 38px; line-height: 1.1;
  }
  .badge {
    position: absolute; width: 172px; height: 172px; border-radius: 50%;
    background: var(--mauve); color: var(--white);
    display: flex; align-items: center; justify-content: center; text-align: center;
    font-weight: 500; font-size: 21px; line-height: 1.4;
  }
  .badge--fees { left: 349px; top: 291px; }
  .badge--minimum { left: 476px; top: 425px; }
  .badge--friday { left: 674px; top: 495px; font-weight: 600; font-size: 22px; text-transform: uppercase; }
  .feature { position: absolute; left: 47px; top: 430px; color: var(--plum); }
  .feature__name { font-family: var(--hand); font-size: 82px; line-height: 1; letter-spacing: 1px; }
  .feature__price { font-family: var(--hand); font-size: 44px; line-height: 1; margin-top: 4px; }
  .feature__desc {
    margin-top: 16px; color: var(--orchid); font-weight: 600; font-size: 21.5px; line-height: 1.38; text-transform: uppercase; width: 540px;
  }
  .feature__desc span { text-transform: none; }
  .extra-title {
    position: absolute; left: 0; right: 0; top: 702px; text-align: center;
    color: var(--white); font-family: var(--hand); font-size: 62px; line-height: 76px; letter-spacing: 1px;
  }
  .menu { position: absolute; left: 28px; top: 785px; width: 903px; height: 286px; display: flex; }
  .menu__col { position: relative; flex: 1; padding: 16px 0 0 50px; background: var(--blush); }
  .menu__col--toppings { background: var(--lavender); }
  .menu__title { font-family: var(--hand); font-size: 66px; line-height: 1; color: var(--plum); }
  .menu__title small { font-size: 36px; margin-left: 4px; }
  .menu__list { list-style: none; margin-top: 14px; font-weight: 600; font-size: 19.5px; line-height: 26px; color: var(--mauve); }
  .menu__col--toppings .menu__list { color: var(--plum); }
  .menu__note {
    position: absolute; left: 0; right: 0; bottom: 0; height: 74px;
    background: var(--plum-deep); color: var(--white);
    display: flex; align-items: center; justify-content: center; text-align: center;
    font-weight: 500; font-size: 16px; line-height: 1.3;
  }
  .menu__note--left { clip-path: polygon(0 0, 100% 0, 100% 40%, 90% 100%, 0 100%); }
  .menu__note--right { clip-path: polygon(0 0, 100% 0, 100% 100%, 10% 100%, 0 40%); }
  .website {
    position: absolute; left: 0; right: 0; top: 1084px; text-align: center;
    color: var(--plum); font-weight: 700; font-size: 30px; letter-spacing: 4.6px;
  }
  .footer { position: absolute; left: 0; right: 0; bottom: 0; height: 72px; display: flex; }
  .footer__call {
    width: 675px; background: var(--plum-deep); color: var(--white);
    display: flex; align-items: center; justify-content: center; gap: 14px;
    font-weight: 600; font-size: 40px; border-right: 5px solid var(--white);
  }
  .footer__call .lead { font-family: var(--hand); font-size: 42px; }
  .footer__social {
    flex: 1; background: var(--mauve); color: var(--white);
    display: flex; align-items: center; justify-content: center; gap: 10px;
    font-weight: 600; font-size: 26px;
  }
  .footer__dot { width: 26px; height: 26px; border-radius: 50%; border: 3px solid var(--white); }
</style>
</head>
<body>
<main class="flyer">
  <svg class="decor" width="960" height="1200" viewBox="0 0 960 1200" aria-hidden="false">
    <defs>
      <radialGradient id="bowlTones" cx="45%" cy="50%" r="60%">
        <stop offset="0%" stop-color="#eadfcf"/>
        <stop offset="45%" stop-color="#c9b8a8"/>
        <stop offset="75%" stop-color="#c7434f"/>
        <stop offset="100%" stop-color="#5c7a86"/>
      </radialGradient>
    </defs>
    <!-- photo frame arcs -->
    <path d="M500 480 A255 255 0 0 1 640 20" fill="none" stroke="var(--mauve)" stroke-width="8"/>
    <path d="M520 460 A245 245 0 0 1 690 0" fill="none" stroke="var(--plum-deep)" stroke-width="6"/>
    <path d="M620 530 Q760 570 900 528" fill="none" stroke="var(--plum-deep)" stroke-width="4"/>
    <circle cx="755" cy="255" r="240" fill="url(#bowlTones)" role="img" aria-label="Photo of an açaí bowl topped with banana slices, blueberries, strawberries, granola and coconut"/>
    <!-- brand ring -->
    <circle cx="203" cy="259" r="140" fill="none" stroke="var(--orchid)" stroke-width="7"/>
    <!-- green brush band -->
    <path d="M40 708 L880 698 L905 712 L870 722 L930 740 L860 752 L900 770 L40 778 L10 770 L60 756 L30 742 L70 728 L25 716 Z" fill="var(--leaf-deep)"/>
  </svg>

  <div class="brand">Berry<br>Good Bites</div>

  <div class="badge badge--fees">No hidden<br>delivery<br>fees</div>
  <div class="badge badge--minimum">5 bowl<br>or smoothie<br>minimum</div>
  <div class="badge badge--friday">Friday<br>deliveries<br>only</div>

  <section class="feature">
    <h1 class="feature__name">Açaí Bowl</h1>
    <p class="feature__price">$9.00</p>
    <p class="feature__desc"><span>Açaí</span> sorbet topped with granola, bananas, strawberries, blueberries, coconut shavings and drizzled with honey</p>
  </section>

  <h2 class="extra-title">Want to add something extra?</h2>

  <section class="menu">
    <div class="menu__col menu__col--fruits">
      <h3 class="menu__title">Fruits <small>$1.00</small></h3>
      <ul class="menu__list"><li>Bananas</li><li>Strawberries</li><li>Blueberries</li></ul>
      <p class="menu__note menu__note--left">Online ordering through website:<br>https://shopkiosk.example<br>/store/berrygoodbites</p>
    </div>
    <div class="menu__col menu__col--toppings">
      <h3 class="menu__title">Toppings <small>.50¢</small></h3>
      <ul class="menu__list"><li>Almonds</li><li>Chia Seeds</li><li>Hemp Seeds</li><li>Cacao Nibs</li><li>Quinoa Puffs</li><li>Coconut Shavings</li><li>Granola</li></ul>
    </div>
    <div class="menu__col menu__col--drizzle">
      <h3 class="menu__title">Drizzle <small>.50¢</small></h3>
      <ul class="menu__list"><li>Peanut Butter</li><li>Almond Butter</li><li>Honey</li><li>Agave</li></ul>
      <p class="menu__note menu__note--right">For the month of February<br>Get one free topping<br>and drizzle!</p>
    </div>
  </section>

  <p class="website">www.berrygoodbites.example</p>

  <footer class="footer">
    <div class="footer__call"><span class="lead">Questions?</span> Call (555) 417-9832</div>
    <div class="footer__social"><span class="footer__dot"></span>@bgbites</div>
  </footer>
</main>
</body>
</html>
```